Swimming Pool Business Billboard

10' x 24' Billboard displaying company name, logo and phone number. Picture of swimming pool activity; kids playing , swimming, etc. Bullet points possibly shown: New Construction, Repairs, Weekly maintenance.

Industry/Entity Type

Swimming pool construction, repairs and maintenance.

Font styles to use
Sans Serif

Colors
0054AA
0677BA
7BADD7
CADEEF
E8F1F8

Requirements
Must have
• Rusty & Calder Pembrook, RUSTY'S POOLS & Service,
Nice to have
• Prefer to have my last name "Pembrook" above the word "POOLS" only in smaller print so that "RUSTYS POOLS" is distinguished.

```html
<!DOCTYPE html>
<html lang="en">
<head>
<meta charset="utf-8">
<title>Rusty's Pools &amp; Services Billboard</title>
<link href="https://fonts.googleapis.com/css2?family=Libre+Baskerville:ital,wght@0,700;1,400&family=Open+Sans:wght@700;800&display=swap" rel="stylesheet">
<style>
  :root {
    --canvas-bg: #b4b4b4;
    --board-white: #ffffff;
    --navy: #0f416b;
    --sky: #7badd7;
    --mist: #e8f1f8;
  }
  html, body {
    margin: 0;
    padding: 0;
    width: 1038px;
    height: 1200px;
    overflow: hidden;
    background: var(--canvas-bg);
  }
  .canvas {
    position: relative;
    width: 1038px;
    height: 1200px;
  }
  .billboard {
    position: absolute;
    left: 19px;
    top: 392px;
    width: 1000px;
    height: 416px;
    display: block;
  }
  .name-script {
    font-family: "Libre Baskerville", serif;
    font-style: italic;
    font-weight: 400;
    fill: var(--navy);
  }
  .company-name {
    font-family: "Libre Baskerville", serif;
    font-weight: 700;
    fill: var(--navy);
  }
  .service-item {
    font-family: "Open Sans", sans-serif;
    font-weight: 700;
    fill: var(--board-white);
    letter-spacing: 1.5px;
  }
  .phone-number {
    font-family: "Open Sans", sans-serif;
    font-weight: 800;
    fill: var(--board-white);
  }
  .brand-mark-text {
    font-family: "Libre Baskerville", serif;
    font-weight: 700;
    fill: var(--navy);
  }
</style>
</head>
<body>
<div class="canvas">
  <svg class="billboard" viewBox="0 0 856 356" xmlns="http://www.w3.org/2000/svg">
    <defs>
      <linearGradient id="poolPhotoTone" x1="0" y1="0" x2="0" y2="1">
        <stop offset="0" stop-color="#f2f0ea"/>
        <stop offset="0.3" stop-color="#dfe6e4"/>
        <stop offset="0.4" stop-color="#2e6b55"/>
        <stop offset="0.47" stop-color="#1f8a8a"/>
        <stop offset="0.55" stop-color="#6ecfe6"/>
        <stop offset="0.8" stop-color="#3cc0e4"/>
        <stop offset="1" stop-color="#24b2de"/>
      </linearGradient>
      <linearGradient id="phoneBandTone" x1="0" y1="0" x2="1" y2="0">
        <stop offset="0" stop-color="#0f416b"/>
        <stop offset="0.6" stop-color="#1d5586"/>
        <stop offset="1" stop-color="#8fb9dc"/>
      </linearGradient>
      <clipPath id="photoShape">
        <polygon points="0,0 212,0 398,356 0,356"/>
      </clipPath>
    </defs>

    <rect class="board-base" x="0" y="0" width="856" height="356" fill="var(--board-white)"/>

    <rect class="pool-photo" x="0" y="0" width="400" height="356" fill="url(#poolPhotoTone)" clip-path="url(#photoShape)" role="img" aria-label="Photo of a smiling girl in a red swim cap splashing in a bright blue swimming pool"/>

    <g class="brand-mark">
      <circle cx="46" cy="44" r="16" fill="var(--navy)"/>
      <text class="brand-mark-text" x="22" y="86" font-size="13">RUSTY'S</text>
    </g>

    <g class="accent-stripes" fill="var(--navy)">
      <polygon points="205,0 214,0 260,86 251,86"/>
      <polygon points="220,0 229,0 275,86 266,86"/>
      <polygon points="343,250 352,250 406,356 397,356"/>
      <polygon points="358,250 367,250 421,356 412,356"/>
    </g>

    <polygon class="services-band" points="237,106 296,106 310,132 856,132 856,252 312,252" fill="var(--navy)"/>

    <polygon class="phone-band" points="393,283 856,283 856,356 430,356" fill="url(#phoneBandTone)"/>

    <text class="name-script" x="570" y="48" font-size="29" text-anchor="middle">Rusty Pembrook</text>
    <text class="company-name" x="568" y="99" font-size="34" text-anchor="middle" textLength="514" lengthAdjust="spacingAndGlyphs">RUSTY'S POOLS &amp; Services</text>

    <text class="service-item" x="409" y="176" font-size="28" text-anchor="middle">Repairs</text>
    <text class="service-item" x="670" y="176" font-size="28" text-anchor="middle">New Construction</text>
    <text class="service-item" x="581" y="221" font-size="28" text-anchor="middle">Weekly maintenance</text>

    <text class="phone-number" x="634" y="341" font-size="60" text-anchor="middle">912-555-0147</text>
  </svg>
</div>
</body>
</html>
```